Scientific project description

Here is a project description related to cellular mechanics, showing above the forces acting on cells in the tissues of our body. The forces on single cells are there to depict how forces are acting on cells (pressure squeezes the cell, shear flow is pushing the upward parts of the cell, tension pulls one part of the cell, strain is stretching the whole cell; the single cell images are to be found also on the last page). Intense red/purple are used to indicate that the forces are stressful (the colors to be used do not need to be exactly like these colors). The picture in the middle is a view of cells (same picture on next page if that needs to be modified). At the left, a description of what happens when everything is going well, i.e. the body stays healthy. At the right, if you dysfunction you get disease. Green nuances were used to indicate health, brownish, perhaps not so pleasant nuances were used to indicate disease. Below are the steps of the project.

On the whole, we're rather happy with the concept description as such, but it should look a little bit nicer. To many color nuances give a "noisy" impression, fonts could be nicer, layout more crisp, and the text on the steps should be more readable. We would also like to have two versions of the same picture, one with black background, one with white.

Target Market(s)

Scientists that are evaluating our project

Requirements
Must have
• Easy to grasp the idea, easy to read and understand the underlying idea.
Nice to have
• Would be good to have the Concept title ("Vorlint Concept and Envisioned Project Progression) on top of the figure as indicated in the second brief picture submitted.

```html
<!DOCTYPE html>
<html lang="en">
<head>
<meta charset="utf-8">
<title>Vorlint Concept and Envisioned Project Progression</title>
<link rel="stylesheet" href="https://fonts.googleapis.com/css2?family=Saira:wght@400;500;800&display=swap">
<style>
  :root {
    --ink: #2b2b2b;
    --white: #ffffff;
    --pressure: #a81f27;
    --shear: #8b1a2c;
    --tension: #7e161b;
    --strain: #6e2571;
    --icon-tint: rgba(255, 255, 255, 0.16);
    --health-dark: #1a3d22;
    --health: #3dbb87;
    --disease-dark: #7d3d1e;
    --disease: #f6b286;
    --arrow: #555555;
    --step-bar: #3a3b3f;
    --step-riser: #c9c9c9;
    --micro-dark: #0c1a0e;
  }
  * { box-sizing: border-box; margin: 0; padding: 0; }
  html, body {
    width: 1200px; height: 666px; overflow: hidden;
    background: var(--white);
    font-family: "Saira", sans-serif;
    color: var(--ink);
  }
  .canvas { position: relative; width: 1200px; height: 666px; }
  .title {
    position: absolute; left: 0; width: 1160px; top: 20px;
    text-align: center; font-size: 32px; font-weight: 500; letter-spacing: 0.3px;
  }
  .diagram { position: absolute; inset: 0; }
  .force-label { font-size: 18px; fill: var(--white); text-anchor: middle; letter-spacing: 0.5px; }
  .force-visual { fill: var(--icon-tint); }
  .label { font-size: 18px; fill: var(--ink); text-anchor: middle; letter-spacing: 0.3px; }
  .node-text { font-size: 18px; fill: var(--white); text-anchor: middle; letter-spacing: 0.8px; }
  .outcome-text { font-size: 18px; fill: var(--ink); text-anchor: middle; letter-spacing: 0.8px; }
  .hub-text { font-size: 22px; font-weight: 800; fill: var(--white); text-anchor: middle; letter-spacing: 1.6px; }
  .step-text { font-size: 17px; fill: var(--white); text-anchor: middle; letter-spacing: 1px; }
</style>
</head>
<body>
<main class="canvas">
  <h1 class="title">Vorlint Concept and Envisioned Project Progression</h1>

  <svg class="diagram" width="1200" height="666" viewBox="0 0 1200 666">
    <defs>
      <radialGradient id="micrograph" cx="50%" cy="50%" r="60%">
        <stop offset="0%" stop-color="#2e6e2c"/>
        <stop offset="55%" stop-color="#1d4a1f"/>
        <stop offset="100%" stop-color="var(--micro-dark)"/>
      </radialGradient>
      <marker id="arrowhead" markerWidth="8" markerHeight="8" refX="4" refY="4" orient="auto">
        <path d="M0,0 L8,4 L0,8 z" fill="var(--arrow)"/>
      </marker>
      <marker id="arrowhead-dark" markerWidth="8" markerHeight="8" refX="4" refY="4" orient="auto">
        <path d="M0,0 L8,4 L0,8 z" fill="var(--ink)"/>
      </marker>
    </defs>

    <g class="force-band">
      <polygon points="211,72 415,72 415,174 211,203" fill="var(--pressure)"/>
      <rect x="415" y="72" width="168" height="102" fill="var(--shear)"/>
      <rect x="583" y="72" width="168" height="102" fill="var(--tension)"/>
      <polygon points="751,72 955,72 955,203 751,174" fill="var(--strain)"/>

      <text class="force-label" x="307" y="96">Pressure</text>
      <text class="force-label" x="499" y="96">Shear</text>
      <text class="force-label" x="661" y="96">Tension</text>
      <text class="force-label" x="847" y="96">Strain</text>

      <rect class="force-visual" x="256" y="102" width="112" height="68" rx="6" role="img" aria-label="Cell squeezed flat by downward pressure arrows"/>
      <rect class="force-visual" x="462" y="100" width="88" height="62" rx="6" role="img" aria-label="Cell pushed sideways by shear flow arrows"/>
      <rect class="force-visual" x="620" y="100" width="82" height="62" rx="6" role="img" aria-label="Cell pulled upward by tension arrows"/>
      <rect class="force-visual" x="762" y="122" width="184" height="34" rx="6" role="img" aria-label="Elongated cell stretched by outward strain arrows"/>
    </g>
    <text class="label" x="893" y="221">Forces on cells</text>

    <ellipse cx="581" cy="298" rx="124" ry="113" fill="url(#micrograph)" role="img" aria-label="Fluorescence micrograph of cells with green cytoskeleton and red focal adhesions"/>
    <text class="hub-text" x="581" y="301">Mechanostasis</text>

    <line x1="439" y1="294" x2="362" y2="294" stroke="var(--arrow)" stroke-width="3" marker-end="url(#arrowhead)"/>
    <text class="label" x="404" y="282">Cell fitness</text>
    <line x1="718" y1="294" x2="796" y2="294" stroke="var(--arrow)" stroke-width="3"/>
    <text class="label" x="760" y="282">Cell frailty</text>

    <circle cx="273" cy="308" r="74" fill="var(--health-dark)"/>
    <text class="node-text" x="273" y="289">Functional</text>
    <text class="node-text" x="273" y="313">cellular</text>
    <text class="node-text" x="273" y="337">machineries</text>
    <line x1="273" y1="386" x2="273" y2="406" stroke="var(--ink)" stroke-width="3" marker-end="url(#arrowhead-dark)"/>
    <circle cx="273" cy="471" r="52" fill="var(--health)"/>
    <text class="outcome-text" x="273" y="477">Health</text>

    <circle cx="894" cy="308" r="74" fill="var(--disease-dark)"/>
    <text class="node-text" x="894" y="289">Dysfunctional</text>
    <text class="node-text" x="894" y="313">cellular</text>
    <text class="node-text" x="894" y="337">machineries</text>
    <line x1="894" y1="386" x2="894" y2="406" stroke="var(--ink)" stroke-width="3" marker-end="url(#arrowhead-dark)"/>
    <circle cx="893" cy="471" r="52" fill="var(--disease)"/>
    <text class="outcome-text" x="893" y="477">Disease</text>

    <g class="steps">
      <polygon points="499,444 667,444 679,456 487,456" fill="var(--step-riser)"/>
      <polygon points="487,480 679,480 691,492 475,492" fill="var(--step-riser)"/>
      <polygon points="475,516 691,516 703,528 463,528" fill="var(--step-riser)"/>
      <polygon points="463,552 703,552 715,564 451,564" fill="var(--step-riser)"/>
      <polygon points="451,588 715,588 727,600 439,600" fill="var(--step-riser)"/>
      <polygon points="439,624 727,624 739,636 427,636" fill="var(--step-riser)"/>

      <rect x="499" y="420" width="168" height="24" fill="var(--step-bar)"/>
      <rect x="487" y="456" width="192" height="24" fill="var(--step-bar)"/>
      <rect x="475" y="492" width="216" height="24" fill="var(--step-bar)"/>
      <rect x="463" y="528" width="240" height="24" fill="var(--step-bar)"/>
      <rect x="451" y="564" width="264" height="24" fill="var(--step-bar)"/>
      <rect x="439" y="600" width="288" height="24" fill="var(--step-bar)"/>
      <rect x="427" y="636" width="312" height="24" fill="var(--step-bar)"/>

      <text class="step-text" x="583" y="439">Therapies</text>
      <text class="step-text" x="577" y="475">Prevention</text>
      <text class="step-text" x="577" y="511">Critical targets</text>
      <text class="step-text" x="577" y="547">Cellular machineries</text>
      <text class="step-text" x="577" y="583">Disease models</text>
      <text class="step-text" x="583" y="619">Cell, tissue &amp; organ responses</text>
      <text class="step-text" x="583" y="655">Mechanical force models</text>
    </g>
  </svg>
</main>
</body>
</html>
```